Poster / Flyer / Advertisement for Frosk Brew Chill (Unique Product!)

We’re selling alcoholic (7.5%) flavored ice for beer…for example, you might try our Lime flavor in a Valdor. We need a great ad/poster…please follow these guidelines:
USE THE PRODUCT PHOTO & KEEP IT SIMPLE!
Use the attached “action shot” of our product prominently. I prefer just the glass of beer, so turn off the layer with the beer bottle. Photoshop in a great background and KEEP IT SIMPLE - the product shot pretty much says it all. Find a great background, add the words “Your beer is getting warm”, and layer in some of our branding (see below). That’s it! Don’t make the poster too busy!
USE OUR CURRENT BRANDING
I’ve attached AI files with all of our branding. Layer in the pattern used on the packaging, our logo, and probably the “Frosk Chill” banner. Also, given that our most popular flavor is Lime in a Valdor, I would look for a background that helps express that (just a thought, it’s up to you to make it look good!).
MAKE IT VERSATILE
We need this to be versatile and easily scale up or down in size for various applications such as:
1) Large format poster for the front window of a convenience store
2) Smaller format for poster ads in bars/restaurants
3) Even smaller format for window clings that go on the glass doors of beer coolers
I also want the words for the poster to be easily changeable for the different applications:
1) Bar – I would use the tagline “Your beer is getting warm”
2) Convenience Store – I would use the line “Don’t drink warm beer…check the freezer!” or something similar. Just need it easy to change
Updates
Project Deadline Extended
Reason: Still deciding on designs. Need time to review with business partners. Thanks all!
Target Market(s)
Beer drinkers - especially those that like fruity beers like summer shandy
Industry/Entity Type
Brewery
Font styles to use
Other font styles liked:
- Use attached fonts!
Colors
Designer to choose colors to be used in the design.
Requirements
Must have
- Use the product shot and our branding...and a simple design!
Nice to have
- Want a "drinking an ice cold beer on a summer day" feel to this.

```html
<!DOCTYPE html>
<html lang="en">
<head>
<meta charset="utf-8">
<title>Frosk Brew Chill – Your Beer Is Getting Warm</title>
<link rel="stylesheet" href="https://fonts.googleapis.com/css2?family=Roboto+Condensed:wght@700;800&display=swap">
<style>
  :root {
    --page-bg: #eeeeee;
    --sun-yellow: #ffd60a;
    --ray-yellow: #ffe23d;
    --glow-yellow: #fff07a;
    --ink: #231f20;
    --paper: #ffffff;
    --beer-light: #fff3a6;
    --beer-deep: #e9b90c;
  }
  * { margin: 0; padding: 0; box-sizing: border-box; }
  html, body {
    width: 1200px;
    height: 1200px;
    overflow: hidden;
    background: var(--page-bg);
  }
  .poster {
    position: absolute;
    left: 220px;
    top: 30px;
    width: 830px;
    height: 1244px;
    transform: scale(0.9164);
    transform-origin: top left;
    background: var(--sun-yellow);
    overflow: hidden;
  }
  .poster__art {
    position: absolute;
    inset: 0;
    width: 830px;
    height: 1244px;
  }
  .headline {
    font-family: "Roboto Condensed", "Arial Narrow", sans-serif;
    font-weight: 800;
    fill: var(--ink);
  }
  .steps__label {
    font-family: "Roboto Condensed", "Arial Narrow", sans-serif;
    font-weight: 700;
    font-size: 25px;
    letter-spacing: 0.5px;
    fill: var(--paper);
  }
  .brand__name {
    font-family: "Roboto Condensed", "Arial Narrow", sans-serif;
    font-weight: 800;
    font-size: 34px;
    letter-spacing: 1px;
    fill: var(--ink);
  }
</style>
</head>
<body>
<div class="poster">
  <svg class="poster__art" viewBox="0 0 830 1244" xmlns="http://www.w3.org/2000/svg">
    <defs>
      <radialGradient id="centerGlow" cx="415" cy="672" r="520" gradientUnits="userSpaceOnUse">
        <stop offset="0" stop-color="var(--glow-yellow)" stop-opacity="0.55"/>
        <stop offset="1" stop-color="var(--sun-yellow)" stop-opacity="0"/>
      </radialGradient>
      <linearGradient id="beerFill" x1="0" y1="0" x2="1" y2="0">
        <stop offset="0" stop-color="var(--beer-deep)"/>
        <stop offset="0.5" stop-color="var(--beer-light)"/>
        <stop offset="1" stop-color="var(--beer-deep)"/>
      </linearGradient>
      <polygon id="ray" points="415,672 345,-340 485,-340"/>
    </defs>

    <!-- sunburst background -->
    <g class="sunburst" fill="var(--ray-yellow)">
      <use href="#ray" transform="rotate(0 415 672)"/>
      <use href="#ray" transform="rotate(24 415 672)"/>
      <use href="#ray" transform="rotate(48 415 672)"/>
      <use href="#ray" transform="rotate(72 415 672)"/>
      <use href="#ray" transform="rotate(96 415 672)"/>
      <use href="#ray" transform="rotate(120 415 672)"/>
      <use href="#ray" transform="rotate(144 415 672)"/>
      <use href="#ray" transform="rotate(168 415 672)"/>
      <use href="#ray" transform="rotate(192 415 672)"/>
      <use href="#ray" transform="rotate(216 415 672)"/>
      <use href="#ray" transform="rotate(240 415 672)"/>
      <use href="#ray" transform="rotate(264 415 672)"/>
      <use href="#ray" transform="rotate(288 415 672)"/>
      <use href="#ray" transform="rotate(312 415 672)"/>
      <use href="#ray" transform="rotate(336 415 672)"/>
    </g>
    <rect width="830" height="1244" fill="url(#centerGlow)"/>

    <!-- headline -->
    <text class="headline" x="95" y="432" font-size="158" textLength="488" lengthAdjust="spacingAndGlyphs">YOUR BE</text>
    <rect class="product-shot" role="img" aria-label="Product photo: a pint glass of pale beer with a frozen lime ice wedge splashing into it"
          x="553" y="157" width="122" height="275" rx="6" fill="url(#beerFill)"/>
    <text class="headline" x="670" y="432" font-size="158" textLength="70" lengthAdjust="spacingAndGlyphs">R</text>
    <text class="headline" x="103" y="617" font-size="162" textLength="637" lengthAdjust="spacingAndGlyphs">IS GETTING</text>
    <text class="headline" x="105" y="857" font-size="264" textLength="635" lengthAdjust="spacingAndGlyphs">WARM</text>

    <!-- how-to banner -->
    <g class="steps">
      <path d="M0 1092 H590 Q604 1133 596 1174 H0 Z" fill="var(--ink)"/>
      <!-- freeze -->
      <g class="steps__icon" stroke="var(--paper)" stroke-width="4" stroke-linecap="round">
        <line x1="81" y1="1120" x2="81" y2="1150"/>
        <line x1="68" y1="1127.5" x2="94" y2="1142.5"/>
        <line x1="68" y1="1142.5" x2="94" y2="1127.5"/>
      </g>
      <text class="steps__label" x="113" y="1144">FREEZE</text>
      <line x1="222" y1="1114" x2="222" y2="1154" stroke="var(--paper)" stroke-width="2.5"/>
      <!-- drop -->
      <g class="steps__icon" stroke="var(--paper)" stroke-width="2.5" fill="none">
        <rect x="252" y="1124" width="22" height="22" rx="3" transform="rotate(20 263 1135)"/>
        <line x1="259" y1="1101" x2="259" y2="1112"/>
        <line x1="264" y1="1101" x2="264" y2="1112"/>
        <line x1="269" y1="1101" x2="269" y2="1112"/>
      </g>
      <text class="steps__label" x="295" y="1144">DROP</text>
      <line x1="381" y1="1114" x2="381" y2="1154" stroke="var(--paper)" stroke-width="2.5"/>
      <!-- enjoy -->
      <g class="steps__icon" stroke="var(--paper)" stroke-width="2.5" fill="none">
        <rect x="418" y="1120" width="24" height="30" rx="3"/>
        <path d="M442 1126 h6 a4 4 0 0 1 4 4 v8 a4 4 0 0 1 -4 4 h-6"/>
        <line x1="426" y1="1128" x2="426" y2="1144"/>
        <line x1="434" y1="1128" x2="434" y2="1144"/>
      </g>
      <text class="steps__label" x="462" y="1144">ENJOY</text>
    </g>

    <!-- brand -->
    <g class="brand">
      <circle cx="652" cy="1132" r="16" fill="var(--ink)"/>
      <text class="brand__name" x="678" y="1144">FROSK</text>
    </g>
  </svg>
</div>
</body>
</html>
```